Business Card Design

Professional solutions in (servers, security, networks, programming)

Industry/Entity Type

Business

Contact Information for Business Card

Tarek Hounayni
Internet services and network solutions
DPV - RTLK - RTLB
netcare@qo-lam.com / 05917406238
www.qo-lam.com

```html
<!DOCTYPE html>
<html lang="en">
<head>
<meta charset="utf-8">
<title>Business Card – Tarek Hounayni</title>
<link href="https://fonts.googleapis.com/css2?family=Open+Sans:wght@400;700&display=swap" rel="stylesheet">
<style>
  :root {
    --backdrop: #e6e4e0;
    --card: #fbfbfa;
    --ink: #1d3f4e;
    --muted: #8c9296;
    --icon: #7d8488;
  }
  html, body {
    margin: 0;
    width: 1200px;
    height: 1022px;
    overflow: hidden;
    background: var(--backdrop);
  }
  .business-card {
    position: absolute;
    left: 150px;
    top: 251px;
    width: 900px;
    height: 520px;
    background: var(--card);
    border-radius: 22px;
    box-shadow: 0 6px 24px rgba(0,0,0,0.12);
    font-family: "Open Sans", Arial, sans-serif;
    color: var(--ink);
  }
  .contact-block {
    position: absolute;
    left: 72px;
    bottom: 72px;
  }
  .person-name {
    margin: 0;
    font-weight: 700;
    font-size: 30px;
    letter-spacing: 1.5px;
    text-transform: uppercase;
    line-height: 1;
  }
  .credentials {
    margin: 8px 0 18px;
    font-size: 15px;
    color: var(--muted);
    letter-spacing: 0.5px;
  }
  .contact-list {
    list-style: none;
    margin: 0;
    padding: 0;
  }
  .contact-list li {
    display: flex;
    align-items: center;
    gap: 10px;
    font-size: 18px;
    line-height: 27px;
    color: var(--ink);
  }
  .contact-icon {
    width: 13px;
    height: 13px;
    flex: none;
  }
  .brand-block {
    position: absolute;
    right: 72px;
    top: 110px;
  }
  .brand-name {
    margin: 0;
    font-family: "Open Sans", Arial, sans-serif;
    font-weight: 700;
    font-size: 62px;
    line-height: 1;
    letter-spacing: 1px;
    color: var(--ink);
  }
  .brand-tagline {
    margin: 14px 0 0 3px;
    font-size: 22px;
    color: var(--muted);
    line-height: 1.2;
  }
  .brand-tagline-spaced {
    margin: 6px 0 0 3px;
    font-size: 18px;
    letter-spacing: 15px;
    color: var(--muted);
    line-height: 1.2;
  }
</style>
</head>
<body>
  <section class="business-card">
    <div class="brand-block">
      <h2 class="brand-name">KELVANE CO</h2>
      <p class="brand-tagline">Internet services and network</p>
      <p class="brand-tagline-spaced">solutions</p>
    </div>

    <div class="contact-block">
      <h1 class="person-name">Tarek Hounayni</h1>
      <p class="credentials">DPV - RTLK - RTLB</p>
      <ul class="contact-list">
        <li>
          <svg class="contact-icon" viewBox="0 0 16 16" aria-hidden="true"><path fill="var(--icon)" d="M3 1l3 3-1.5 2c1 2 3.5 4.5 5.5 5.5L12 10l3 3-2 2C7 14 2 9 1 3z"/></svg>
          05917406238
        </li>
        <li>
          <svg class="contact-icon" viewBox="0 0 16 16" aria-hidden="true"><rect x="1" y="3" width="14" height="10" fill="none" stroke="var(--icon)" stroke-width="1.6"/><path d="M1 3l7 6 7-6" fill="none" stroke="var(--icon)" stroke-width="1.6"/></svg>
          netcare@qo-lam.com
        </li>
        <li>
          <svg class="contact-icon" viewBox="0 0 16 16" aria-hidden="true"><circle cx="8" cy="8" r="7" fill="var(--icon)"/><path d="M1 8h14M8 1c-3 3-3 11 0 14M8 1c3 3 3 11 0 14" fill="none" stroke="var(--card)" stroke-width="1"/></svg>
          www.qo-lam.com
        </li>
      </ul>
    </div>
  </section>
</body>
</html>
```